Recycling Depot Business Card Design

We need a double sided business card for our recycling depot business. Please include name, position, address, phone, cell, fax, email and website address. Business card should match the colour scheme of our logo and look environmental but modern. I've attached a few business cards from Mintvale Works that I like.

Industry/Entity Type

Recycling

Contact Information for Business Card

Please include name, position, address, phone, cell, fax, email and website address.

Font styles to use
Sans Serif

Requirements
Must have
• Our Logo, Colour Scheme that matches our logo. Use of Colour Gradients and a custom look.

```html
<!DOCTYPE html>
<html lang="en">
<head>
<meta charset="utf-8">
<title>Greenloop Materials – Business Card</title>
<link rel="stylesheet" href="https://fonts.googleapis.com/css2?family=Lato:wght@400;700&display=swap">
<style>
  :root {
    --bg: #d6d6d6;
    --paper: #ffffff;
    --green-dark: #1a5c32;
    --green-mid: #2a7a45;
    --green-light: #8dc63f;
    --green-back-a: #14502a;
    --green-back-b: #33805a;
    --ink: #3a3a3a;
    --rule: #6f6f6f;
  }
  * { box-sizing: border-box; margin: 0; padding: 0; }
  html, body { width: 1200px; height: 1200px; overflow: hidden; }
  body {
    background: var(--bg);
    font-family: "Lato", sans-serif;
    position: relative;
  }
  .card {
    position: absolute;
    left: 262px;
    width: 686px;
    height: 392px;
    border-radius: 18px;
    overflow: hidden;
  }
  .card-front { top: 165px; background: var(--paper); }
  .card-back {
    top: 653px;
    background: linear-gradient(45deg, var(--green-back-a) 0%, var(--green-mid) 60%, var(--green-back-b) 100%);
  }
  .brand {
    position: absolute;
    right: 47px;
    top: 70px;
    display: flex;
    align-items: center;
    gap: 10px;
  }
  .brand-dot {
    width: 30px; height: 30px; border-radius: 50%;
    background: var(--green-mid);
  }
  .brand-name {
    font-weight: 700;
    font-size: 30px;
    color: var(--green-mid);
    letter-spacing: -0.5px;
  }
  .person { position: absolute; left: 44px; top: 207px; }
  .person-name { font-weight: 700; font-size: 23px; color: var(--green-dark); line-height: 1.1; }
  .person-role { font-size: 16px; color: var(--green-light); margin-top: 1px; filter: brightness(0.85); }
  .rule {
    position: absolute; left: 44px; right: 47px; top: 262px;
    height: 1px; background: var(--rule);
  }
  .contacts {
    position: absolute; left: 44px; top: 276px;
    list-style: none; font-size: 16px; color: var(--ink); line-height: 19.5px;
  }
  .contacts li { display: flex; align-items: center; gap: 9px; }
  .contacts svg { width: 12px; height: 12px; fill: var(--green-dark); flex: none; }
  .address {
    position: absolute; right: 47px; top: 276px;
    text-align: right; font-size: 16px; color: var(--ink); line-height: 19.5px;
  }
  .address .company { color: var(--green-dark); font-weight: 700; font-size: 16px; }
  .front-band {
    position: absolute; left: 0; right: 0; bottom: 0; height: 10px;
    background: var(--green-dark);
  }
  .front-band-light {
    position: absolute; right: 0; bottom: 0; height: 10px; width: 238px;
    background: linear-gradient(90deg, #4e9a3a, var(--green-light));
    border-left: 3px solid var(--paper);
    transform: skewX(-12deg); transform-origin: bottom right;
  }
  .back-brand {
    position: absolute; left: 0; right: 0; top: 150px;
    display: flex; justify-content: center; align-items: center; gap: 14px;
  }
  .back-brand .brand-dot { width: 40px; height: 40px; background: var(--paper); }
  .back-brand .brand-name { color: var(--paper); font-size: 40px; }
  .back-url {
    position: absolute; left: 0; right: 0; top: 340px;
    text-align: center; color: var(--paper);
    font-size: 16px; letter-spacing: 5px;
  }
</style>
</head>
<body>
  <section class="card card-front">
    <div class="brand">
      <span class="brand-dot"></span>
      <span class="brand-name">Greenloop Materials</span>
    </div>
    <div class="person">
      <div class="person-name">Daniel Harper</div>
      <div class="person-role">President</div>
    </div>
    <div class="rule"></div>
    <ul class="contacts">
      <li><svg viewBox="0 0 12 12"><path d="M2.5 0.5l2 2.5-1.2 1.3c.7 1.6 2 2.9 3.6 3.6L8.2 6.7l2.6 2-1 2.6C4.8 11.2.8 7.2.5 2.2z"/></svg>428-610-3372</li>
      <li><svg viewBox="0 0 12 12"><path d="M3 0h6v12H3zM4 1.5v8h4v-8z"/></svg>428-774-1905</li>
      <li><svg viewBox="0 0 12 12"><path d="M3 0h6v4H3zM0 5h12v5H0zM2 8h8v4H2z"/></svg>428-610-3380</li>
      <li><svg viewBox="0 0 12 12"><path d="M0 2.5h12v7H0zM0.8 3.2L6 7l5.2-3.8"/></svg>hello@greenloop.co</li>
    </ul>
    <div class="address">
      <div class="company">Greenloop Materials</div>
      <div>2140 Fernhill Road</div>
      <div>Juneau, Alaska 99801</div>
      <div>www.greenloop.co</div>
    </div>
    <div class="front-band"></div>
    <div class="front-band-light"></div>
  </section>

  <section class="card card-back">
    <div class="back-brand">
      <span class="brand-dot"></span>
      <span class="brand-name">Greenloop Materials</span>
    </div>
    <div class="back-url">WWW.GREENLOOP.CO</div>
  </section>
</body>
</html>
```